brightleafwell.com and taverclinic.com

I'd like to do a web design re-make on two of our websites. Brightleafwell.com is focused on selling nutriceutical products (private labeled by brightleafwell.com), and provide an expert blog to give great advices on general health.

Taverclinic.com is a site for Dr. Taver's new medicine clinic. It should be integrated with brightleafwell.com. Clients can directly make appointments on the site, and order products from brightleafwell.com.

Target Market(s)

Middle to upper

Industry/Entity Type

Clinic

Number of Pages Required

4 page

Font styles to use
Serif
Sans Serif

Colors
0254a3
0792cd
33a6d7
00a98f
33b7a4
acd036
9bcb3c
cadf82

Requirements
Must have
• Home page tabs: About Dr. Taver, Store, Blog, Videos, Appointment
• Home page content should include: a promotional section (with moving features), an appointment book (for online appointment booking), a product section (for store), and a blog section.
Nice to have
• The look and feel should be modern, professional, trustworthy, zen.
Should not have
• Real pictures of people, except for Dr. Taver.

```html
<!DOCTYPE html>
<html lang="en">
<head>
<meta charset="utf-8">
<title>Brightleaf Well — Home</title>
<link href="https://fonts.googleapis.com/css2?family=Roboto:wght@300;400;500;700&display=swap" rel="stylesheet">
<style>
:root{
  --blue:#1e9ad6;
  --blue-dark:#0b7fc0;
  --ink:#333333;
  --muted:#777777;
  --line:#d9d9d9;
  --soft:#f2f2f2;
  --footer:#2f2f2f;
  --white:#ffffff;
  --btn-dark:#555555;
}
*{box-sizing:border-box;margin:0;padding:0}
html,body{width:1200px;height:3462px;overflow:hidden;background:var(--white)}
body{font-family:'Roboto',Arial,sans-serif;color:var(--ink);position:relative}

/* header */
.site-header{position:absolute;left:0;top:0;width:1200px;height:130px;background:var(--white)}
.brand{position:absolute;left:40px;top:22px;width:170px;font-size:34px;font-weight:500;line-height:34px;color:var(--ink)}
.search{position:absolute;left:640px;top:23px;width:326px;height:30px;border:2px solid #cfcfcf;border-radius:15px}
.search svg{position:absolute;right:10px;top:6px}
.login{position:absolute;left:995px;top:17px;width:130px;height:32px;background:var(--blue);color:var(--white);font-size:14px;text-align:center;line-height:32px}
.main-nav{position:absolute;left:0;top:72px;width:1200px;height:58px}
.main-nav a{position:absolute;top:0;height:58px;line-height:58px;font-size:14px;color:var(--ink);text-decoration:none;text-transform:uppercase;text-align:center;white-space:nowrap}
.main-nav a.active{background:var(--blue);color:var(--white)}

/* hero */
.hero{position:absolute;left:0;top:130px;width:1200px;height:756px;background:linear-gradient(90deg,#c9a993 0%,#e3c9b7 35%,#dfe2e6 60%,#b7c0c9 100%)}
.hero-title{position:absolute;left:650px;top:180px;color:var(--white);font-weight:400;line-height:1.05}
.hero-title .l1{font-size:82px;display:block}
.hero-title .l2{font-size:54px;display:block;font-weight:300;margin-top:10px}
.hero-title .l3{font-size:82px;display:block;margin-top:6px}
.hero-title .l3 small{font-size:56px}
.hero-arrows{position:absolute;left:808px;top:520px}
.hero-dots{position:absolute;left:842px;top:672px}

/* about */
.about{position:absolute;left:0;top:886px;width:1200px;height:398px;background:var(--soft)}
.section-title{position:absolute;font-weight:400;text-transform:uppercase}
.about h2{left:60px;top:34px;font-size:40px;color:var(--ink)}
.about h2 span{color:var(--blue);font-size:52px}
.about-photo{position:absolute;left:100px;top:120px;width:176px;height:176px;border-radius:50%;border:6px solid var(--blue);background:radial-gradient(circle at 50% 40%,#c9a58c 0%,#7a5a4a 55%,#3a3a3a 100%)}
.about-text{position:absolute;left:323px;top:126px;width:820px;font-size:14.5px;line-height:21px;color:var(--muted)}
.about-text p{margin-bottom:14px}
.btn-blue{position:absolute;background:var(--blue);color:var(--white);font-size:14px;text-align:center;text-transform:uppercase}
.about .btn-blue{left:540px;top:340px;width:178px;height:44px;line-height:44px}

/* appointment */
.appointment{position:absolute;left:0;top:1284px;width:1200px;height:225px;background:var(--blue)}
.appointment h2{left:0;width:1200px;text-align:center;top:40px;font-size:28px;color:var(--white);font-weight:500}
.field{position:absolute;top:101px;width:332px;height:37px;background:var(--white);font-size:13px;color:#aaa;line-height:37px;padding-left:12px}
.btn-book{position:absolute;left:519px;top:167px;width:220px;height:49px;line-height:49px;background:var(--btn-dark);color:var(--white);font-size:14px;text-align:center;text-transform:uppercase}

/* products */
.products h2{left:50px;top:1612px;font-size:32px;color:var(--ink)}
.rule{position:absolute;height:2px;background:var(--line)}
.card{position:absolute;width:248px;height:433px;border:2px solid #e2e2e2;background:var(--white);text-align:center}
.card.featured{border-color:#c8c8c8;box-shadow:0 0 6px rgba(0,0,0,.18)}
.badge{position:absolute;left:84px;top:-2px;width:80px;height:28px;line-height:28px;background:var(--blue);color:var(--white);font-size:13px}
.bottle{position:absolute;left:59px;top:48px;width:130px;height:160px;border-radius:16px 16px 8px 8px;background:linear-gradient(90deg,#c9cfd8,#f4f5f7 45%,#b9c0cb)}
.price{position:absolute;left:0;width:100%;top:238px;font-size:32px;color:var(--blue);font-weight:500}
.pname{position:absolute;left:0;width:100%;top:284px;font-size:16px;font-weight:700;text-transform:uppercase;white-space:nowrap}
.meta{position:absolute;left:0;width:100%;top:312px;font-size:13px;line-height:19px;color:var(--muted)}
.cart{position:absolute;left:52px;top:368px;width:144px;height:46px;line-height:46px;border:2px solid #dedede;color:var(--muted);font-size:13px;text-transform:uppercase}
.cart.active{background:var(--blue);border-color:var(--blue);color:var(--white)}
.pager{position:absolute;top:2637px;display:flex;gap:6px;left:920px}
.pager span{width:44px;height:44px;border:1px solid var(--line);font-size:14px;text-align:center;line-height:44px;color:var(--muted)}

/* blog + videos */
.media{position:absolute;left:0;top:2726px;width:1200px;height:434px;background:#f7f7f7}
.media h2{top:58px;font-size:32px;color:var(--ink)}
.divider{position:absolute;left:597px;top:58px;height:360px;border-left:2px dashed #9fcbe6}
.thumb{position:absolute}
.post-title{position:absolute;font-size:14px;color:var(--blue);text-transform:uppercase;text-align:center;width:400px}
.post-text{position:absolute;font-size:14px;line-height:20px;color:var(--muted);text-align:center;width:400px}
.see-all{position:absolute;width:145px;height:44px;line-height:44px;background:var(--blue);color:var(--white);font-size:14px;padding-left:32px}
.see-all svg{position:absolute;right:14px;top:16px}

/* footer */
.site-footer{position:absolute;left:0;top:3160px;width:1200px;height:302px;background:var(--footer);color:var(--white)}
.site-footer .brand{position:absolute;left:52px;top:22px;color:var(--white)}
.tagline{position:absolute;left:52px;top:144px;width:250px;font-size:14px;line-height:19px;color:#ddd}
.copy{position:absolute;left:52px;top:235px;font-size:11px;color:#aaa}
.contact-title{position:absolute;left:485px;top:14px;font-size:15px;font-weight:700}
.contact{position:absolute;left:485px;font-size:14px;color:#ddd;line-height:20px}
.contact .txt{position:absolute;left:50px;top:0;white-space:nowrap}
.phone-num{font-size:28px;color:var(--white);font-weight:500}
.social{position:absolute;left:830px;top:72px;display:flex;gap:30px}
.social span{width:48px;height:48px;border-radius:50%;background:var(--white);display:block}
</style>
</head>
<body>

<header class="site-header">
  <div class="brand">Brightleaf<br>Well</div>
  <div class="search"><svg width="16" height="16" viewBox="0 0 16 16"><circle cx="6.5" cy="6.5" r="5" fill="none" stroke="#333" stroke-width="2"/><line x1="10" y1="10" x2="15" y2="15" stroke="#333" stroke-width="2"/></svg></div>
  <div class="login">LOGIN</div>
  <nav class="main-nav">
    <a class="active" style="left:254px;width:112px">Home</a>
    <a style="left:372px;width:150px">About Dr. Taver</a>
    <a style="left:595px;width:80px">Store</a>
    <a style="left:740px;width:80px">Blog</a>
    <a style="left:880px;width:90px">Videos</a>
    <a style="left:1030px;width:110px">Appointment</a>
  </nav>
</header>

<section class="hero" role="img" aria-label="Promotional photo of a calm woman with hands on her cheeks, soft grey backdrop">
  <h1 class="hero-title">
    <span class="l1">Empowering</span>
    <span class="l2">Your Ageless</span>
    <span class="l3">Body <small>and</small> Mind</span>
  </h1>
  <svg class="hero-arrows" width="132" height="54" viewBox="0 0 132 54">
    <rect x="0" y="0" width="62" height="54" rx="4" fill="#fff"/>
    <rect x="70" y="0" width="62" height="54" rx="4" fill="#fff"/>
    <path d="M36 17 L26 27 L36 37" fill="none" stroke="#333" stroke-width="4"/>
    <path d="M96 17 L106 27 L96 37" fill="none" stroke="#333" stroke-width="4"/>
  </svg>
  <svg class="hero-dots" width="62" height="18" viewBox="0 0 62 18">
    <circle cx="9" cy="9" r="7" fill="#fff"/><circle cx="31" cy="9" r="7" fill="#fff" opacity=".6"/><circle cx="53" cy="9" r="7" fill="#fff" opacity=".6"/>
  </svg>
</section>

<section class="about">
  <h2 class="section-title">About <span>Dr. Taver</span></h2>
  <div class="about-photo" role="img" aria-label="Portrait of Dr. Lena Taver"></div>
  <div class="about-text">
    <p>Dr. Lena Taver, as thousands of patients refer to as "Dr. Taver" or "the Healer", brings a great combination between modern medical sciences and ancient medicine. Every smile, hug and encouraging word from her in addition to her sincerely caring and loving nature give those in need tremendous healing power!</p>
    <p>Here's a brief introduction for Dr. Taver's background:</p>
    <p style="margin:0">M.D. from Eastbrook University, Clinical Medicine<br>M.S. from Harborview University, Medical Human Physiology<br>Post Doctor Research Associate, University of Mesa Verde, Cancer Center<br>PhD Oriental Medicine</p>
  </div>
  <div class="btn-blue">Read More</div>
</section>

<section class="appointment">
  <h2 class="section-title">Make an Appointment</h2>
  <div class="field" style="left:101px">Name</div>
  <div class="field" style="left:447px">Phone Number</div>
  <div class="field" style="left:793px">Email Address</div>
  <div class="btn-book">Make Appointment</div>
</section>

<section class="products">
  <h2 class="section-title">Products</h2>
  <div class="rule" style="left:50px;top:1662px;width:1100px"></div>

  <div class="card featured" style="left:58px;top:1725px"><div class="badge">NEW</div><div class="bottle" role="img" aria-label="Supplement bottle"></div><div class="price">$60.00</div><div class="pname">Adrenavita</div><div class="meta">SKU: BLW0100<br>120 Capsules</div><div class="cart active">Add to Cart</div></div>
  <div class="card" style="left:335px;top:1725px"><div class="badge">SALE</div><div class="bottle" role="img" aria-label="Supplement bottle"></div><div class="price">$35.00</div><div class="pname">Aller Calm</div><div class="meta">SKU: BLW0200<br>60 Capsules</div><div class="cart">Add to Cart</div></div>
  <div class="card" style="left:614px;top:1725px"><div class="badge">SALE</div><div class="bottle" role="img" aria-label="Supplement bottle"></div><div class="price">$60.00</div><div class="pname">Auto Poise</div><div class="meta">SKU: BLW0300<br>120 Capsules</div><div class="cart">Add to Cart</div></div>
  <div class="card" style="left:891px;top:1725px"><div class="badge">SALE</div><div class="bottle" role="img" aria-label="Supplement bottle"></div><div class="price">$35.00</div><div class="pname">B Comp Prime</div><div class="meta">SKU: BLW0400<br>60 Capsules</div><div class="cart">Add to Cart</div></div>

  <div class="card" style="left:58px;top:2181px"><div class="badge">NEW</div><div class="bottle" role="img" aria-label="Supplement bottle"></div><div class="price">$40.00</div><div class="pname">Beauty Glow</div><div class="meta">SKU: BLW0500<br>120 Capsules</div><div class="cart">Add to Cart</div></div>
  <div class="card" style="left:335px;top:2181px"><div class="badge">SALE</div><div class="bottle" role="img" aria-label="Supplement bottle"></div><div class="price">$40.00</div><div class="pname">Candiclear</div><div class="meta">SKU: BLW0700<br>60 Capsules</div><div class="cart">Add to Cart</div></div>
  <div class="card" style="left:614px;top:2181px"><div class="badge">SALE</div><div class="bottle" role="img" aria-label="Supplement bottle"></div><div class="price">$50.00</div><div class="pname">Cardio Vital Support</div><div class="meta">SKU: BLW0800<br>60 Capsules</div><div class="cart">Add to Cart</div></div>
  <div class="card" style="left:891px;top:2181px"><div class="badge">SALE</div><div class="bottle" role="img" aria-label="Supplement bottle"></div><div class="price">$30.00</div><div class="pname">Clear Breath</div><div class="meta">SKU: BLW0900<br>60 Capsules</div><div class="cart">Add to Cart</div></div>

  <div class="pager"><span>&laquo;</span><span>1</span><span>2</span><span>3</span><span>&raquo;</span></div>
</section>

<section class="media">
  <h2 class="section-title" style="left:50px">Blog</h2>
  <div class="rule" style="left:50px;top:108px;width:520px"></div>
  <h2 class="section-title" style="left:629px">Videos</h2>
  <div class="rule" style="left:629px;top:108px;width:520px"></div>
  <div class="divider"></div>

  <svg class="thumb" style="left:86px;top:181px" width="440" height="44" viewBox="0 0 440 44">
    <circle cx="22" cy="22" r="21" fill="#1e9ad6"/><path d="M25 14 L17 22 L25 30" fill="none" stroke="#fff" stroke-width="3"/>
    <circle cx="413" cy="22" r="21" fill="#1e9ad6"/><path d="M410 14 L418 22 L410 30" fill="none" stroke="#fff" stroke-width="3"/>
  </svg>
  <div class="thumb" style="left:231px;top:116px;width:202px;height:144px;background:linear-gradient(135deg,#f3efe9,#d9c6b4 60%,#c2d6e6)" role="img" aria-label="Blog photo of a woman with a lab flask"></div>
  <div class="post-title" style="left:132px;top:278px">Oque penatibus et magnis dis parturient</div>
  <div class="post-text" style="left:132px;top:300px">The purpose of the Lakeside Biopharma Statistics Workshop is to foster discussion on statistical methodology in the...</div>
  <svg class="thumb" style="left:225px;top:352px" width="160" height="30" viewBox="0 0 160 30">
    <circle cx="14" cy="15" r="11" fill="none" stroke="#1e9ad6" stroke-width="2.5"/><path d="M14 9 V15 H19" fill="none" stroke="#1e9ad6" stroke-width="2.5"/>
    <text x="34" y="20" font-family="Roboto, sans-serif" font-size="14" fill="#777">12/2014</text>
    <path d="M104 7 H126 V21 H112 L106 26 V21 H104 Z" fill="#1e9ad6"/>
    <text x="134" y="20" font-family="Roboto, sans-serif" font-size="14" fill="#777">04</text>
  </svg>
  <div class="see-all" style="left:403px;top:384px">See All<svg width="8" height="12" viewBox="0 0 8 12"><path d="M0 0 L8 6 L0 12 Z" fill="#fff"/></svg></div>

  <svg class="thumb" style="left:638px;top:190px" width="500" height="60" viewBox="0 0 500 60">
    <path d="M22 4 L4 30 L22 56" fill="none" stroke="#1e9ad6" stroke-width="3"/>
    <path d="M478 4 L496 30 L478 56" fill="none" stroke="#1e9ad6" stroke-width="3"/>
  </svg>
  <div class="thumb" style="left:730px;top:130px;width:323px;height:130px;background:linear-gradient(90deg,#2a2a2a,#6b6b6b 45%,#d8c5b8)" role="img" aria-label="Video still of a woman in profile"></div>
  <svg class="thumb" style="left:871px;top:175px" width="40" height="40" viewBox="0 0 40 40"><circle cx="20" cy="20" r="20" fill="#fff"/><path d="M15 11 L29 20 L15 29 Z" fill="#333"/></svg>
  <div class="post-title" style="left:690px;top:278px">Oque penatibus et magnis dis parturient</div>
  <div class="post-text" style="left:690px;top:300px">The purpose of the Lakeside Biopharma Statistics Workshop is to foster discussion on statistical methodology in the...</div>
  <div class="see-all" style="left:972px;top:378px">See All<svg width="8" height="12" viewBox="0 0 8 12"><path d="M0 0 L8 6 L0 12 Z" fill="#fff"/></svg></div>
</section>

<footer class="site-footer">
  <div class="brand">Brightleaf<br>Well</div>
  <div class="tagline">Feel young, look beautiful, filled with energy, free of pain, be happy and joyful!</div>
  <div class="copy">&copy; Copyright 2014 by Brightleaf Well | All Rights Reserved.</div>
  <div class="contact-title">Contact Details</div>
  <div class="contact" style="top:48px">
    <svg width="22" height="30" viewBox="0 0 22 30"><path d="M11 0 C4.9 0 0 4.9 0 11 C0 19 11 30 11 30 S22 19 22 11 C22 4.9 17.1 0 11 0 Z" fill="#fff"/><circle cx="11" cy="11" r="4" fill="#2f2f2f"/></svg>
    <div class="txt">1180 Harbor View Rd, Suite C<br>Seaside Bay, CA</div>
  </div>
  <div class="contact" style="top:116px">
    <svg width="26" height="26" viewBox="0 0 26 26"><path d="M6 1 L10 8 L7 11 C9 15 11 17 15 19 L18 16 L25 20 L22 25 C11 25 1 15 1 4 Z" fill="#fff"/></svg>
    <div class="txt phone-num" style="top:-4px">949 - 555 - 0142</div>
  </div>
  <div class="contact" style="top:188px">
    <svg width="26" height="18" viewBox="0 0 26 18"><rect x="1" y="1" width="24" height="16" fill="none" stroke="#fff" stroke-width="2"/><path d="M1 1 L13 10 L25 1" fill="none" stroke="#fff" stroke-width="2"/></svg>
    <div class="txt">hello@taverclinic.com</div>
  </div>
  <div class="social" role="img" aria-label="Social network links"><span></span><span></span><span></span><span></span></div>
</footer>

</body>
</html>
```